Zielgruppe
Der Honig soll in 35g Gläschen als kleines Gastgeschenk ausgegeben und darüber hinaus an im privaten Umfeld in 250g Gläsern verkauft werden.
Corporate Identity des Betriebes ist nicht zu beachten, da dies mein persönliches Hobby ist
Aufgabenstellung
Der Name des Honigs : MOOSTALGOLD
"gewonnen auf dem Dach Köln Altstadt"
Alle auf dem Etikett vorgeschrieben Angaben wie Menge (250g ; 35g), Name/Adresse des Imkers
Mindestens Haltbar bis + Leerfeld/Platz um Datum einzustempeln...gerne auch kreative Lösung um Stempel zu vermeiden
"Ursprungsland: Deutschland" oder "Deutscher Honig"
"Vor Licht und Wärme geschützt lagern"
Es werden Etiketten für zwei Füllmengen (250g und 35g Probierglas) benötigt.
Desweiteren werden für die 250g Gläser Gewähretiketten benötigt die sich am Etikettendesign orientieren und die Sorte angeben - Sommerhonig / Sommerblüte
Alternativ kann die Sorte auch auf dem Etikett angegeben werden
Ergänzung:
Etikettengröße für 250g Höhe max. 4cm x Breite max 10cm
Etikettengröße Probierglas Höhe max 2cm x Breite 8-10cm

```html
<!DOCTYPE html>
<html lang="de">
<head>
<meta charset="utf-8">
<title>Moostalgold Etikett 250 g</title>
<link rel="stylesheet" href="https://fonts.googleapis.com/css2?family=Oswald:wght@300;400;600;700&display=swap">
<style>
  :root {
    --sky: #7fb0c4;
    --white: #ffffff;
    --honey: #f2e27a;
    --honey-pale: #f6eda8;
    --honey-band: #f0e38c;
    --ink-blue: #6f9fb4;
  }
  * { margin: 0; padding: 0; box-sizing: border-box; }
  html, body { width: 1200px; height: 472px; overflow: hidden; background: var(--sky); }
  .label {
    position: relative;
    width: 1200px;
    height: 472px;
    background: var(--sky);
    font-family: "Oswald", sans-serif;
    overflow: hidden;
  }
  .legal-info {
    position: absolute;
    left: 14px;
    top: 412px;
    width: 280px;
    transform-origin: 0 0;
    transform: rotate(-90deg);
    color: var(--honey-pale);
    font-weight: 300;
    font-size: 22px;
    line-height: 35px;
    letter-spacing: 0.3px;
    white-space: nowrap;
  }
  .crest {
    position: absolute;
    left: 470px;
    top: 40px;
    width: 260px;
    height: 230px;
  }
  .product-name {
    position: absolute;
    left: 0;
    width: 1200px;
    top: 256px;
    text-align: center;
    color: var(--white);
    font-weight: 700;
    font-size: 66px;
    line-height: 1.2;
    letter-spacing: 2px;
  }
  .variety {
    position: absolute;
    left: 0;
    width: 1200px;
    top: 336px;
    text-align: center;
    color: var(--honey);
    font-weight: 400;
    font-size: 23px;
    line-height: 30px;
    letter-spacing: 2px;
  }
  .ornament-rule {
    position: absolute;
    left: 522px;
    top: 374px;
    width: 156px;
    height: 8px;
    border-radius: 4px;
    background: var(--white);
    opacity: 0.9;
  }
  .butterfly {
    position: absolute;
    left: 808px;
    top: 304px;
    width: 82px;
    height: 72px;
    border-radius: 40% 50% 45% 40%;
    background: var(--honey);
  }
  .content-amount {
    position: absolute;
    left: 1104px;
    top: 408px;
    width: 230px;
    transform-origin: 0 0;
    transform: rotate(-90deg);
    color: var(--white);
    font-weight: 300;
    line-height: 76px;
    white-space: nowrap;
  }
  .content-amount .amount-label { font-size: 24px; margin-right: 8px; }
  .content-amount .amount-value { font-size: 54px; font-weight: 400; }
  .footer-band {
    position: absolute;
    left: 0;
    top: 417px;
    width: 1200px;
    height: 55px;
    background: linear-gradient(90deg, var(--honey-band), var(--honey-pale) 50%, var(--honey-band));
  }
  .beekeeper-contact {
    position: absolute;
    left: 0;
    width: 1200px;
    top: 427px;
    text-align: center;
    color: var(--ink-blue);
    font-weight: 300;
    font-size: 23px;
    line-height: 34px;
    letter-spacing: 0.3px;
  }
</style>
</head>
<body>
<main class="label">
  <div class="legal-info">
    <p>Ursprungsland:</p>
    <p>Deutschland</p>
    <p>Vor Licht und Wärme</p>
    <p>geschützt lagern</p>
    <p>Mindestens Haltbar bis:</p>
  </div>

  <svg class="crest" viewBox="0 0 260 230">
    <defs>
      <path id="crest-arc" d="M 39 182 A 105 105 0 1 1 221 182"/>
    </defs>
    <text fill="#f6eda8" font-family="Oswald, sans-serif" font-weight="300" font-size="19" letter-spacing="0.4">
      <textPath href="#crest-arc" startOffset="50%" text-anchor="middle">Gewonnen auf den Dächern der Domblick Altstadt</textPath>
    </text>
    <rect role="img" aria-label="Illustration der Kölner Domtürme" x="102" y="52" width="56" height="140" rx="4" fill="#ffffff" opacity="0.92"/>
  </svg>

  <h1 class="product-name">MOOSTALGOLD</h1>
  <p class="variety">SOMMERBLÜTE</p>
  <div class="ornament-rule" role="img" aria-label="Zierleiste aus Perlen"></div>
  <div class="butterfly" role="img" aria-label="Illustration eines gelben Schmetterlings"></div>

  <p class="content-amount"><span class="amount-label">Inhalt:</span><span class="amount-value">250 g</span></p>

  <div class="footer-band" role="img" aria-label="Wabenmuster in Honiggelb"></div>
  <p class="beekeeper-contact">Tobias Brandl · Lindenhofweg 14 · 50667 Köln · Tel.: 0170 5558214</p>
</main>
</body>
</html>
```